VARDO Web

To design a look and feel for a website. The company offers technical services to governemtns and public bodies. It does NOT market to the public.

The core business is GIS (Geographic Information Systems)

The site needs to be clean and simple, The current version is available here: www.varduna.ie

Target Market(s)

Goverment agencies and public bodies in the EU, buying through the public procurerment process

Requirements
Should not have
• corny graphics of hands holding globes or sateliites please.

```html
<!DOCTYPE html>
<html lang="en">
<head>
<meta charset="utf-8">
<title>The VARDO Group – GIS Data Management</title>
<link href="https://fonts.googleapis.com/css2?family=PT+Sans:wght@400;700&family=Noto+Sans:wght@400&display=swap" rel="stylesheet">
<style>
:root{
  --brand:#1f80b9;
  --brand-dark:#175f8c;
  --brand-light:#5aaee0;
  --ink:#111;
  --paper:#fff;
  --panel:#eeeeee;
}
*{margin:0;padding:0;box-sizing:border-box}
html,body{width:1100px;height:1200px;overflow:hidden;background:var(--paper)}
body{font-family:"PT Sans",sans-serif;color:var(--ink)}
.page{position:absolute;left:0;top:0;width:1000px;height:1091px;transform:scale(1.1);transform-origin:0 0}
.site-header{position:absolute;left:73px;top:0;width:857px;height:87px;background:var(--brand);border-radius:0 0 4px 4px}
.brand{position:absolute;left:16px;top:14px;display:flex;align-items:center;gap:6px;color:var(--paper);font-weight:700;font-size:18px}
.brand-dot{width:11px;height:11px;border-radius:50%;background:var(--paper)}
.main-nav{position:absolute;right:18px;top:54px;display:flex}
.main-nav a{color:var(--paper);text-decoration:none;font-size:15px;padding:1px 14px;line-height:20px}
.main-nav a.active{background:var(--paper);color:var(--brand);border-radius:5px;padding:1px 18px}
.hero{position:absolute;left:72px;top:98px;width:858px;height:220px;background:linear-gradient(100deg,#e9f1f7 0%,#7fbde4 25%,#2f82bd 55%,#1f80b9 80%)}
.hero-title{position:absolute;right:27px;top:85px;color:var(--paper);font-size:21px;text-align:right}
.hero-sub{position:absolute;right:27px;top:113px;color:var(--paper);font-size:12px;font-weight:700}
.hero-shadow{position:absolute;left:72px;top:318px;width:846px;height:9px;background:linear-gradient(#aaa,#eee);border-radius:0 0 50% 50%}
.section-title{position:absolute;left:0;width:985px;text-align:center;font-size:20px;font-weight:400}
.service{position:absolute;top:386px;width:170px}
.service-visual{height:66px;margin:0 auto;border-radius:3px}
.service h3{font-weight:400;font-size:15px;text-align:center;margin-top:6px;line-height:16px}
.service p{font-family:"Noto Sans",sans-serif;font-size:11px;line-height:14.5px;margin-top:1px}
.read-more{position:absolute;top:173px;width:75px;height:15px;border-radius:5px;background:var(--brand);color:var(--paper);font-family:"Noto Sans",sans-serif;font-size:9.5px;text-align:center;line-height:15px}
.welcome{position:absolute;left:138px;top:638px;width:728px;font-family:"Noto Sans",sans-serif;font-size:11px;line-height:14.4px}
.welcome p{margin-bottom:14.4px}
.client-arrow{position:absolute;top:945px;width:29px;height:29px}
.clients{position:absolute;top:925px;left:160px;width:680px;height:70px}
.client{position:absolute;top:0;height:70px;display:flex;align-items:center;justify-content:center;gap:5px;color:var(--brand);font-size:14px;font-weight:700;white-space:nowrap}
.client-mark{width:10px;height:10px;border-radius:50%;background:var(--brand);flex:none}
.client.boxed{background:var(--panel)}
.site-footer{position:absolute;left:72px;top:1031px;width:858px;height:60px;background:var(--brand)}
.copyright{position:absolute;left:16px;top:25px;color:var(--paper);font-size:12px;font-weight:700}
.footer-nav{position:absolute;right:20px;top:22px;display:flex}
.footer-nav a{color:var(--paper);text-decoration:none;font-size:15px;padding:0 11px}
</style>
</head>
<body>
<div class="page">
  <header class="site-header">
    <div class="brand"><span class="brand-dot"></span>The VARDO Group</div>
    <nav class="main-nav">
      <a class="active" href="#">Home</a><a href="#">Services</a><a href="#">Clients</a><a href="#">Contact</a><a href="#">Inspir</a>
    </nav>
  </header>

  <section class="hero" role="img" aria-label="Map of northern Europe in shades of blue">
    <div class="hero-title">VARDO leads the way in GIS</div>
    <div class="hero-sub">Data Management and Web Systems Development</div>
  </section>
  <div class="hero-shadow"></div>

  <h2 class="section-title" style="top:347px">Our Services</h2>

  <div class="service" style="left:135px">
    <div class="service-visual" role="img" aria-label="Server tower" style="width:46px;background:linear-gradient(#3d8fd1,#1b5e9a)"></div>
    <h3>Data Management</h3>
    <p>VARDO has extensive experience in Spatial Data processing. Services include&nbsp; Raw data capture, Geocoding, Re-projection...</p>
    <div class="read-more" style="left:35px">Read More...</div>
  </div>

  <div class="service" style="left:341px">
    <div class="service-visual" role="img" aria-label="Globe" style="width:70px;border-radius:50%;background:radial-gradient(circle at 40% 35%,#cfe8ff,#2c7fd0 55%,#0b3f86)"></div>
    <h3>Spatial Data</h3>
    <p>The rapid development of the use and availability of Spatial Data presents most organisations with opportunity...</p>
    <div class="read-more" style="left:37px">Read More...</div>
  </div>

  <div class="service" style="left:529px">
    <div class="service-visual" role="img" aria-label="Open fields under a blue sky" style="width:98px;background:linear-gradient(#3a7cc6 0%,#a9cdef 60%,#c98a3c 75%,#8a5a25 100%)"></div>
    <h3 style="margin-top:4px">Land using</h3>
    <p style="margin-top:3px">&nbsp;[Agriculture and Forestry] VARDO has a comprehensive range of services on offer to the Agriculture Industry including...</p>
    <div class="read-more" style="left:36px">Read More...</div>
  </div>

  <div class="service" style="left:730px">
    <div class="service-visual" role="img" aria-label="High-speed train on a viaduct" style="width:98px;background:linear-gradient(135deg,#bcd9ee,#5e9fcf 60%,#dfeef8)"></div>
    <h3 style="margin-top:4px">Transport</h3>
    <p style="margin-top:3px;width:135px">VARDO offers advice on route management and fleet asset tracking with EMC reporting...</p>
    <div class="read-more" style="left:28px">Read More...</div>
  </div>

  <h2 class="section-title" style="top:607px;font-size:19px">Welcome To VARDO Group</h2>

  <div class="welcome">
    <p>The VARDO Group has been in business since 1994 and continues to develop and update its range of services. The company has a high level of expertise in handling data and information, and in building and re-engineering database systems. We have a particular expertise in working with Irish data sets and have a strong grounding in dealing with spatial data.</p>
    <p>We also have extensive experience in working in a Brightsoft development environment, both Desktop and WebForge.We have worked on development of small scale systems using Brightsoft products for over 12 years. We have assisted in the migration of systems from Brightsoft Ledger to both QueryBase Server and Orwell DB databases. This has included re-writing code from Macro Basic to either Forge Basic or Cx.</p>
    <p>We have built web sites for our clients using WebForge using Forge.net frameworks 1.5 through to 4.0. VARDO will work with all spatial data formats and systems including Orwell DB, MapTrace/Xtend, Geodyne QueryBase Server. We are not agents for any vendor, preferring to select the components that best suit the project’s needs.</p>
    <p>The company’s Quality Management System is ISO 9001:2008 certified (reviewed Jan 2012).</p>
    <p>The VARDO Group Ltd is registered in ireland number 417293</p>
  </div>

  <h2 class="section-title" style="top:895px;font-size:19px">Our Clients</h2>

  <svg class="client-arrow" style="left:106px" viewBox="0 0 29 29" aria-label="Previous">
    <circle cx="14.5" cy="14.5" r="13" fill="none" stroke="var(--brand)" stroke-width="2.5"/>
    <path d="M18 8 L9 14.5 L18 21 Z" fill="var(--brand)"/>
  </svg>
  <div class="clients">
    <div class="client" style="left:5px;width:82px"><span class="client-mark"></span>Unitas</div>
    <div class="client" style="left:122px;width:116px"><span class="client-mark"></span>statvia</div>
    <div class="client boxed" style="left:275px;width:105px"><span class="client-mark"></span>Harrowmede</div>
    <div class="client" style="left:415px;width:165px"><span class="client-mark"></span>Fernleigh Dept</div>
    <div class="client" style="left:612px;width:72px"><span class="client-mark"></span>Corvane</div>
  </div>
  <svg class="client-arrow" style="left:857px" viewBox="0 0 29 29" aria-label="Next">
    <circle cx="14.5" cy="14.5" r="13" fill="none" stroke="var(--brand)" stroke-width="2.5"/>
    <path d="M11 8 L20 14.5 L11 21 Z" fill="var(--brand)"/>
  </svg>

  <footer class="site-footer">
    <div class="copyright">Copyright © The VARDO group Ltd 2013</div>
    <nav class="footer-nav">
      <a href="#">Home</a><a href="#">Services</a><a href="#">Clients</a><a href="#">Contact</a><a href="#">Inspir</a>
    </nav>
  </footer>
</div>
</body>
</html>
```